Need Landing Page for Data Security Company

Need a new landing page (PSD) for our data security company (www.korvadel.com). We specialize in selling patented hard drive destruction machines that guarantee the data on your hard drives are unrecoverable. We have several large clients such as Lumigrove, Chirpaloo and Vendrix just to name a few. Really want to have a landing page that sticks out.

Attached is a one pager we use just for emailing clients. We do not want the landing page to look like this. This is just for content to read. The landing page needs

Target Market(s)

Government, business corporations, IT decision makers. Not every day user

Industry/Entity Type

It Company

Number of Pages Required

1 page

Font styles to use
Other font styles liked:
• Match Current Website

Requirements
Must have
• Its a landing page so it needs a Contact us Section at the very top!!!
• Need to be a very attractive landing page.. Would like a mix of showcasing our products and also having some client list to show our bigger name clients (lumigrove, vendrix, chirpaloo)
• Landing page needs to use the same color/style schema as current website. Also will be using the same menu structure as what exists today.
• www.korvadel.com
Nice to have
• Maybe some streamvault videos of our products?

```html
<!DOCTYPE html>
<html lang="en">
<head>
<meta charset="utf-8">
<title>Korvadel – Innovative Data Security</title>
<link href="https://fonts.googleapis.com/css2?family=Open+Sans:wght@400;600;700&family=Oswald:wght@500&display=swap" rel="stylesheet">
<style>
:root{
  --green:#8dc63f;
  --green-dark:#6fa52a;
  --black:#0d0d0d;
  --grey:#e4e4e4;
  --grey-mid:#b9b9b9;
  --text:#555;
  --white:#fff;
}
*{box-sizing:border-box;margin:0;padding:0}
html,body{width:849px;height:1200px;overflow:hidden}
body{font-family:"Open Sans",Arial,sans-serif;color:var(--text);background:var(--white);position:relative}
.site-header{height:50px;display:flex;align-items:center;justify-content:space-between;padding:0 44px 0 54px}
.brand{display:flex;flex-direction:column}
.brand-name{font-size:28px;font-weight:700;color:var(--green);line-height:1}
.brand-tag{font-size:7px;color:#888;margin-top:2px}
.main-nav{display:flex;gap:4px}
.main-nav a{border:1px solid #bbb;font-size:9px;color:#333;text-decoration:none;padding:5px 12px}
.hero{height:267px;background:var(--grey);padding:24px 56px}
.hero-frame{height:219px;border:6px solid var(--green);background:var(--white);display:flex;align-items:center;padding:0 22px;gap:26px}
.hero-products{display:flex;gap:8px;align-items:flex-end}
.hero-products div{background:linear-gradient(#f5f5f5,#b8b8b8);border:1px solid #999}
.hero-copy{flex:1;text-align:center}
.hero-copy h1{font-family:"Oswald",sans-serif;font-weight:500;font-size:19px;color:var(--green);letter-spacing:.5px}
.hero-copy p{font-size:8px;line-height:1.5;margin:8px 6px 12px}
.btn{display:inline-block;background:var(--green);color:var(--black);font-size:8px;font-weight:600;padding:5px 14px;text-decoration:none;border:1px solid var(--green-dark)}
.about{height:193px;text-align:center;padding:28px 90px 0}
.section-title{font-size:14px;font-weight:700;color:#333}
.about p{font-size:7.5px;line-height:1.6;margin-top:8px}
.about .btn{margin-top:10px}
.products{height:297px;background:var(--black);text-align:center;padding-top:12px}
.products .section-title{color:var(--green)}
.rule{width:34px;height:2px;background:var(--green);margin:6px auto 0}
.product-list{display:flex;justify-content:center;gap:32px;margin-top:26px}
.product{width:160px}
.product-circle{width:150px;height:150px;border-radius:50%;background:#7c7c7c;border:6px solid var(--white);margin:0 auto;display:flex;align-items:center;justify-content:center}
.product-circle div{width:64px;height:92px;background:linear-gradient(#ededed,#9a9a9a)}
.product h3{color:var(--white);font-size:10px;font-weight:600;margin:12px 0 8px}
.clients{height:143px;text-align:center;padding-top:20px}
.client-row{display:flex;align-items:center;justify-content:center;gap:12px;margin-top:22px}
.arrow{width:18px;height:18px}
.client{width:84px;height:38px;border:1px solid #ccc;display:flex;align-items:center;justify-content:center;font-size:12px;font-weight:700;color:#444}
.client.dark{background:#222;color:var(--white)}
.video{height:148px;background:var(--black);margin-top:7px;display:flex;align-items:center;padding:0 56px;gap:40px}
.video-thumb{width:160px;height:120px;background:linear-gradient(#6a6a6a,#2a2a2a);position:relative}
.video-thumb svg{position:absolute;left:64px;top:44px}
.video-copy h2{color:var(--green);font-size:16px;font-weight:700}
.video-copy .rule{margin:6px 0 0}
.video-copy p{color:#ccc;font-size:8px;line-height:1.6;margin-top:8px;max-width:460px}
.site-footer{display:flex;justify-content:space-between;align-items:center;padding:0 56px;height:52px;margin-top:8px}
.footer-nav{display:flex;gap:24px}
.footer-nav a{font-size:9px;color:#333;text-decoration:none}
.social{display:flex;gap:6px}
.social span{width:9px;height:9px;border-radius:50%;background:#444}
.copyright{border-top:1px solid #ddd;margin:0 56px;text-align:center;font-size:8px;color:#777;padding-top:14px}
</style>
</head>
<body>
<header class="site-header">
  <div class="brand"><span class="brand-name">Korvadel</span><span class="brand-tag">Innovative Data Security</span></div>
  <nav class="main-nav"><a href="#">Home</a><a href="#">About Us ▾</a><a href="#">Products ▾</a><a href="#">Services</a><a href="#">Compliance</a><a href="#">Blog</a><a href="#">Contact</a></nav>
</header>

<section class="hero">
  <div class="hero-frame">
    <div class="hero-products">
      <div role="img" aria-label="Compact drive crusher product" style="width:70px;height:110px"></div>
      <div role="img" aria-label="Drive shredder product" style="width:80px;height:140px"></div>
      <div role="img" aria-label="Degausser product" style="width:70px;height:110px"></div>
    </div>
    <div class="hero-copy">
      <h1>KORVADEL INNOVATIVE SOLUTIONS</h1>
      <p>Korvadel builds certified hard drive destruction systems for agencies, banks and enterprises. Our patented machines crush, shred and degauss media on site, leaving every byte beyond recovery and every audit trail complete.</p>
      <a class="btn" href="#">Read More</a>
    </div>
  </div>
</section>

<section class="about">
  <h2 class="section-title">About Korvadel Technologies</h2>
  <p>Korvadel Technologies, Inc. is a research and engineering firm devoted to secure data elimination for information technology, energy and defense sectors.</p>
  <p>Our company is an innovator in media sanitization, producing shredders, crushers and degaussers trusted by government offices and large corporations. Every product is designed to meet the strictest federal standards for destroying classified information.</p>
  <a class="btn" href="#">Read More</a>
</section>

<section class="products">
  <h2 class="section-title">Our Products</h2>
  <div class="rule"></div>
  <div class="product-list">
    <div class="product"><div class="product-circle"><div role="img" aria-label="Shredline 3SD machine"></div></div><h3>SHREDLINE 3SD</h3><a class="btn" href="#">Read more</a></div>
    <div class="product"><div class="product-circle"><div role="img" aria-label="Shredline HD machine"></div></div><h3>SHREDLINE HD</h3><a class="btn" href="#">Read more</a></div>
    <div class="product"><div class="product-circle"><div role="img" aria-label="Drivepress-HD machine"></div></div><h3>DRIVEPRESS-HD</h3><a class="btn" href="#">Read more</a></div>
    <div class="product"><div class="product-circle"><div role="img" aria-label="Drivepress-HD machine, open"></div></div><h3>DRIVEPRESS-HD</h3><a class="btn" href="#">Read more</a></div>
  </div>
</section>

<section class="clients">
  <h2 class="section-title">Our Clients</h2>
  <div class="rule"></div>
  <div class="client-row">
    <svg class="arrow" viewBox="0 0 18 18"><path d="M11 4 6 9l5 5" fill="none" stroke="#8dc63f" stroke-width="3"/></svg>
    <div class="client">lumigrove</div>
    <div class="client">vendrix</div>
    <div class="client dark">Nordalis</div>
    <div class="client">Chirpaloo</div>
    <div class="client dark">Orbitek</div>
    <div class="client">Quellon</div>
    <svg class="arrow" viewBox="0 0 18 18"><path d="M7 4l5 5-5 5" fill="none" stroke="#8dc63f" stroke-width="3"/></svg>
  </div>
</section>

<section class="video">
  <div class="video-thumb" role="img" aria-label="Product demonstration video still">
    <svg width="32" height="32" viewBox="0 0 32 32"><circle cx="16" cy="16" r="15" fill="rgba(0,0,0,.5)"/><path d="M12 9l11 7-11 7z" fill="#fff"/></svg>
  </div>
  <div class="video-copy">
    <h2>Watch Our Video</h2>
    <div class="rule"></div>
    <p>See how our crushers disable a drive in seconds. This short demo walks through loading, processing and verifying a drive, showing why security teams rely on Korvadel for compliant on-site destruction.</p>
  </div>
</section>

<footer>
  <div class="site-footer">
    <nav class="footer-nav"><a href="#">Home</a><a href="#">About Us</a><a href="#">Products</a><a href="#">Services</a><a href="#">Compliance</a><a href="#">Blog</a><a href="#">Contact</a></nav>
    <div class="social" aria-label="Social links"><span></span><span></span><span></span><span></span></div>
  </div>
  <p class="copyright">©2015 Korvadel, All Rights Reserved.</p>
</footer>
</body>
</html>
```